A property investment company, looking to provide lovely sustainable homes for familys and individua

For a small investment business i am starting which will buy and refurbish unloved houses and apartments to rent out or resell. the company name is my family surname (HARGREAVE). <br/>i would like the design to be simple with maybe some emphasis on an ethical and sustainable/environmentally friendly approach with a branding of maybe trees blended with some houses and or apartments.<br/>The colours i like for this design would be mainly green on either a white or black background.
Target Market(s)
This business card is to be used for professional people such as estate agents
mortgage brokers, solicitors and trades people.
Industry/Entity Type
Real Estate
Contact Information for Business Card
owner/director-Martin hargreave
e-mail-martin@hwlettings.co.uk
website-hargreavehomeholdings.co.uk
mobile-07934560218
landline-02086543107

```html
<!DOCTYPE html>
<html lang="en">
<head>
<meta charset="utf-8">
<title>Hargreave – Business Card</title>
<link href="https://fonts.googleapis.com/css2?family=Noto+Serif:ital,wght@0,400;0,700;1,400&display=swap" rel="stylesheet">
<style>
  :root {
    --page-bg: #e9e6e1;
    --card-dark: #48484b;
    --card-light: #5a5a5e;
    --brand-white: #ffffff;
    --brand-teal: #3cc3ad;
    --brand-lime: #a3d447;
    --icon-ink: #3f3f42;
  }
  * { box-sizing: border-box; margin: 0; padding: 0; }
  html, body {
    width: 1200px; height: 903px; overflow: hidden;
    background: var(--page-bg);
    font-family: "Noto Serif", Georgia, serif;
  }
  .canvas { position: relative; width: 1200px; height: 903px; }
  .card {
    position: absolute;
    width: 520px; height: 300px;
    border-radius: 18px;
    background: radial-gradient(ellipse at 35% 45%, var(--card-light), var(--card-dark) 70%);
    box-shadow: 0 10px 28px rgba(0,0,0,.22);
  }
  .card--front { left: 80px; top: 130px; }
  .card--back  { left: 600px; top: 470px; }

  .front-wordmark {
    position: absolute; inset: 0;
    display: flex; align-items: center; justify-content: center;
    color: var(--brand-white);
    font-weight: 700; font-size: 68px; letter-spacing: .5px;
  }

  .back-wordmark {
    position: absolute; left: 26px; top: 180px;
    color: var(--brand-lime);
    font-weight: 700; font-size: 38px;
  }
  .contact {
    position: absolute; left: 250px; top: 58px;
  }
  .contact__name {
    color: var(--brand-teal); font-weight: 700; font-size: 21px; line-height: 1.1;
  }
  .contact__role {
    color: var(--brand-lime); font-size: 16px; margin: 4px 0 16px 14px;
  }
  .contact__list { list-style: none; }
  .contact__item {
    display: flex; align-items: center; gap: 6px;
    color: var(--brand-teal); font-size: 14.5px; line-height: 1; margin-bottom: 8px;
  }
  .contact__icon { width: 20px; height: 20px; flex: none; }
</style>
</head>
<body>
<main class="canvas">
  <section class="card card--front" aria-label="Card front">
    <div class="front-wordmark">Hargreave</div>
  </section>

  <section class="card card--back" aria-label="Card back">
    <div class="back-wordmark">Hargreave</div>
    <div class="contact">
      <p class="contact__name">Martin hargreave</p>
      <p class="contact__role">owner/director</p>
      <ul class="contact__list">
        <li class="contact__item">
          <svg class="contact__icon" viewBox="0 0 20 20" aria-hidden="true"><circle cx="10" cy="10" r="10" fill="var(--brand-lime)"/><rect x="7" y="4.5" width="6" height="11" rx="1.2" fill="none" stroke="var(--icon-ink)" stroke-width="1.4"/><circle cx="10" cy="13.3" r=".8" fill="var(--icon-ink)"/></svg>
          07934560218
        </li>
        <li class="contact__item">
          <svg class="contact__icon" viewBox="0 0 20 20" aria-hidden="true"><circle cx="10" cy="10" r="10" fill="var(--brand-lime)"/><path d="M5 8.5c0-1.5 2.2-2.5 5-2.5s5 1 5 2.5l-1.8.6-.6-1.4H7.4l-.6 1.4z" fill="var(--icon-ink)"/><rect x="6.5" y="10" width="7" height="4.5" rx="1" fill="var(--icon-ink)"/></svg>
          02086543107
        </li>
        <li class="contact__item">
          <svg class="contact__icon" viewBox="0 0 20 20" aria-hidden="true"><circle cx="10" cy="10" r="10" fill="var(--brand-lime)"/><rect x="5" y="6.5" width="10" height="7" fill="var(--icon-ink)"/><path d="M5 6.5l5 4 5-4" fill="none" stroke="var(--brand-lime)" stroke-width="1"/></svg>
          martin@hwlettings.co.uk
        </li>
        <li class="contact__item">
          <svg class="contact__icon" viewBox="0 0 20 20" aria-hidden="true"><circle cx="10" cy="10" r="10" fill="var(--brand-lime)"/><g fill="none" stroke="var(--icon-ink)" stroke-width="1"><circle cx="10" cy="10" r="5.5"/><ellipse cx="10" cy="10" rx="2.4" ry="5.5"/><path d="M4.5 10h11M5.3 7.3h9.4M5.3 12.7h9.4"/></g></svg>
          hargreavehomeholdings.co.uk
        </li>
      </ul>
    </div>
  </section>
</main>
</body>
</html>
```